Quimby's Yard & Garden Center Business Card Update

I need an updated Business card design for my Lawn and Garden Center. We do Landscaping installs, Lawn Mowing, Snow Removal and also have a Garden Center Retail Division. I uploaded a few of our previous business cards to give an idea of what we are starting with. The main goal of this update is to simplify and modernize the business card, not all of the services that are on the previous cards has to be on the new one but I would still like to highlight our main services. There is also a sample of our logo that Can be used in the design.

Industry/Entity Type

Landscaping

Contact Information for Business Card

Morris Quimby
Morris@Quimbysyardandgarden.example
Business (555) 201-7784
Cell (555) 318-6092

Colors

Designer to choose colors to be used in the design.

Requirements
Must have
• Services Provided :
• Landscaping
• Lawn Maintenance
• Snow Removal
• Garden Center

```html
<!DOCTYPE html>
<html lang="en">
<head>
<meta charset="utf-8">
<title>Quimby's Yard &amp; Garden Center — Business Card</title>
<link rel="stylesheet" href="https://fonts.googleapis.com/css2?family=Chau+Philomene+One&family=Jost:ital,wght@0,400;0,600;1,400&display=swap">
<style>
  :root {
    --front-green: #558a5f;
    --pale-leaf: #c5dd95;
    --back-grey: #e8e8e8;
    --divider: #ffffff;
    --brand-green: #006633;
    --muted-green: #5b8a55;
    --deep-olive: #2f4d1d;
    --ink: #111111;
  }
  * { margin: 0; padding: 0; box-sizing: border-box; }
  html, body { width: 1200px; height: 388px; overflow: hidden; background: var(--back-grey); }
  .card {
    position: relative;
    width: 1200px;
    height: 388px;
    display: flex;
    font-family: "Jost", sans-serif;
  }
  .card-front {
    width: 598px;
    height: 100%;
    background: var(--front-green);
    border-right: 2px solid var(--divider);
    text-align: center;
    color: var(--pale-leaf);
  }
  .front-wordmark {
    font-family: "Jost", sans-serif;
    font-weight: 600;
    font-size: 92px;
    line-height: 1;
    padding-top: 34px;
    letter-spacing: 1px;
  }
  .front-services {
    list-style: none;
    margin-top: 52px;
    font-family: "Chau Philomene One", sans-serif;
    font-size: 38px;
    line-height: 50px;
  }
  .card-back {
    position: relative;
    flex: 1;
    height: 100%;
    background: var(--back-grey);
  }
  .service-strip {
    position: absolute;
    top: 4px;
    left: 6px;
    right: 8px;
    display: flex;
    justify-content: space-between;
    font-size: 19.5px;
    color: var(--muted-green);
    white-space: nowrap;
  }
  .back-wordmark {
    position: absolute;
    top: 82px;
    left: 0;
    right: 0;
    text-align: center;
    font-weight: 600;
    font-size: 112px;
    line-height: 1;
    color: var(--brand-green);
  }
  .contact-person {
    position: absolute;
    left: 10px;
    top: 278px;
    color: var(--ink);
  }
  .contact-name { font-weight: 600; font-size: 21px; line-height: 30px; }
  .contact-email { font-style: italic; font-size: 19px; line-height: 28px; }
  .contact-address {
    position: absolute;
    right: 9px;
    top: 278px;
    text-align: right;
    font-size: 20px;
    line-height: 29px;
    letter-spacing: 0.5px;
    color: var(--muted-green);
  }
  .contact-phones {
    position: absolute;
    left: 10px;
    right: 9px;
    top: 350px;
    display: flex;
    justify-content: space-between;
    font-weight: 600;
    font-size: 25px;
    line-height: 30px;
    color: var(--deep-olive);
    white-space: nowrap;
  }
</style>
</head>
<body>
  <main class="card">
    <section class="card-front">
      <div class="front-wordmark">Quimby's</div>
      <ul class="front-services">
        <li>Garden Center</li>
        <li>Landscaping</li>
        <li>Lawn Maintenance</li>
        <li>Snow Removal</li>
      </ul>
    </section>
    <section class="card-back">
      <div class="service-strip">
        <span>Landscaping</span><span>•</span>
        <span>Lawn Maintenance</span><span>•</span>
        <span>Snow Removal</span><span>•</span>
        <span>Garden Center</span>
      </div>
      <div class="back-wordmark">Quimby's</div>
      <div class="contact-person">
        <p class="contact-name">Morris Quimby</p>
        <p class="contact-email">Morris@Quimbysyardandgarden.example</p>
      </div>
      <address class="contact-address" style="font-style:normal">
        <p>4820 County Road Q</p>
        <p>55512 Millbrook (Ohio)</p>
      </address>
      <div class="contact-phones">
        <span>Business (555) 201-7784</span>
        <span>|</span>
        <span>Cell (555) 318-6092</span>
      </div>
    </section>
  </main>
</body>
</html>
```